Ardent Summit contracting website

I need a website for my storm restoration/roofing contracting company. Looking for design that is in current style with professional details that aren't slammed together. i need something easy to edit my self to keep it fresh and up to date on current information and product. Website needs to have visible and easy to ready contents while keeping the modern, unique, specific, and high quality looks also easy to navigate between pages. My ideal targeted customer are more on the higher end simply due to the work being detailed and most the time custom and modern.

Website needs:

1. Services tab
Inspections - Drone Inspections with AI Damage detections with VOLTRA Software to inspect roofs after storms have impacted customer properties and also annual inspection roofs of every thing on the roof in minutes without having to climb roof manually leading to potential damage.

Residential - Roofing, Roof Repairs, Gutters, Siding, Paint, Decks, and Interior

Commerical - Roofing, Roof Coatings, Roof Maintenance Repair Plans, Roof Repairs, Roofing Gutters, Siding

Those are my most important services that i can think of right now, please set it how ever you think it needs to be set up for easy navigation.

2. Products
Ardent Summit doesn't look at a roof as just a roof. We look at the small details others may ignore or simply dont know anything about them. When we install a roof for clients/customer they are getting a full roofing system that includes only one manufacture per customer selection which qualities every roof installed for the highest material and labor warranty the top material manufactures offer. Ardent Summit carries the highest ranking Certifications with the leading manufacture so our customer can rest easy knowing their roofs were installed with precision.

Brands we love
Hollowbrook Crestline
RVN
Le Morvay

3. Gallery/Recent Projects

Link to sitelens or create folders or whatever for photos to be added weekly or bi weekly

4 . Service Area Map

5. About Us / The Ardent Summit Team

I do not have a domain yet looking for ideas on that as well. The website domain will also be used as the business email @'s

Files attached is the logos and business cards to get idea of the company colors and styles, open to whatever though and will consider everything if it catches my eye and is appealing.

Target Market(s)

Property owners, property management companies, maintenance managers for properties, home owners, business owners, land lords

Industry/Entity Type

Roofing contractor storm restoration home remodel

Coding

Coded - Design and coding required

Number of Pages Required

5+ page

Colors
EB3D1F
EC4F4E
F09395
F8D3D4
FCEDEE

Requirements
Must have
• Design like the RVN roofing manufacturer website or similar

```html
<!DOCTYPE html>
<html lang="en">
<head>
<meta charset="utf-8">
<title>Ardent Summit Contracting</title>
<link href="https://fonts.googleapis.com/css2?family=Bebas+Neue&family=Montserrat:wght@400;500;600;700&display=swap" rel="stylesheet">
<style>
:root{
  --red:#EB3D1F;
  --red-bright:#E8242B;
  --ink:#111111;
  --text:#3a3a3a;
  --muted:#6b6b6b;
  --white:#ffffff;
  --line:#d9d9d9;
  --pink-soft:#FCEDEE;
}
*{box-sizing:border-box;margin:0;padding:0}
html,body{width:1200px;height:4528px;overflow:hidden}
body{position:relative;background:var(--white);font-family:'Montserrat',sans-serif;color:var(--text)}
.abs{position:absolute}
.display{font-family:'Bebas Neue',sans-serif;color:var(--ink);font-weight:400;letter-spacing:.5px}
.eyebrow{font-size:12px;color:var(--red-bright);font-weight:500}
.btn-red{position:absolute;background:var(--red-bright);color:var(--white);font-size:13px;font-weight:500;display:flex;align-items:center;justify-content:center}
.photo{position:absolute}

/* header */
.site-header{position:absolute;left:0;top:0;width:1200px;height:83px;border-bottom:1px solid var(--line)}
.brand{position:absolute;display:flex;align-items:center;gap:8px;font-family:'Bebas Neue',sans-serif;color:var(--ink)}
.brand-mark{width:12px;height:12px;background:var(--red-bright)}
.header-brand{left:88px;top:24px;font-size:30px}
.main-nav{position:absolute;top:34px;left:433px;display:flex;gap:0;font-size:14px;font-weight:500;color:var(--ink)}
.main-nav a{position:absolute;white-space:nowrap;color:inherit;text-decoration:none}
.main-nav .active{color:var(--red-bright);font-weight:700}

/* hero */
.hero-title{left:88px;top:140px;font-size:80px;line-height:76px;width:470px}
.hero-copy{left:88px;top:388px;width:430px;font-size:14px;line-height:25px}
.hero-photo{left:568px;top:83px;width:540px;height:466px;background:linear-gradient(160deg,#c9572a 0%,#a9462a 35%,#6e7b86 60%,#e9e0cd 100%)}
.hero-rule{left:0;top:549px;width:1200px;height:1px;background:var(--line)}

/* about */
.about-photo-a{left:88px;top:679px;width:234px;height:422px;background:linear-gradient(180deg,#b9cfe3 0%,#6d7278 45%,#3b3d40 100%)}
.about-photo-b{left:336px;top:625px;width:182px;height:362px;background:linear-gradient(180deg,#c7c3bf 0%,#a77a5a 55%,#7a5640 100%)}
.years-badge{left:282px;top:999px;width:236px;height:102px;background:var(--ink);color:var(--white);display:flex;align-items:center;justify-content:center;gap:14px}
.years-badge .num{font-family:'Bebas Neue',sans-serif;font-size:66px;line-height:1}
.years-badge .label{font-family:'Bebas Neue',sans-serif;font-size:28px;line-height:26px}
.about-eyebrow{left:554px;top:666px}
.about-title{left:554px;top:690px;font-size:50px;line-height:54px;width:540px}
.about-copy{left:554px;top:820px;width:550px;font-size:14.5px;line-height:28.5px}

/* services */
.services-band{left:0;top:1240px;width:1200px;height:436px;background:var(--red-bright)}
.services-eyebrow{left:88px;top:1284px;font-size:12px;color:var(--white)}
.services-title{left:88px;top:1302px;font-size:54px;line-height:54px;color:var(--white)}
.tab{position:absolute;left:88px;width:206px;height:45px;border:1.5px solid var(--white);color:var(--white);font-size:18px;display:flex;align-items:center;justify-content:center}
.tab.current{background:var(--white);color:var(--ink)}
.service-card{position:absolute;top:1288px;width:225px;height:329px;background:var(--white);padding:0 22px}
.service-card.raised{box-shadow:0 10px 24px rgba(0,0,0,.25)}
.service-card .no{position:absolute;right:14px;top:10px;font-size:14px;font-weight:600;color:var(--ink)}
.service-card svg.icon{position:absolute;left:22px;top:44px}
.service-card h3{position:absolute;left:22px;top:110px;font-family:'Bebas Neue',sans-serif;font-size:38px;font-weight:400;color:var(--ink)}
.service-card p{position:absolute;left:22px;top:164px;width:185px;font-size:13px;line-height:16px;color:var(--text)}
.service-card .go{position:absolute;left:22px;top:290px}

/* products */
.products-eyebrow{left:88px;top:1786px}
.products-title{left:88px;top:1806px;font-size:48px}
.arrow-btn{position:absolute;top:1827px;width:43px;height:36px;display:flex;align-items:center;justify-content:center}
.arrow-btn.outline{left:999px;border:1.5px solid var(--ink)}
.arrow-btn.filled{left:1065px;background:var(--red-bright)}
.product-photo{top:1905px;width:320px;height:218px}
.product-name{position:absolute;top:2146px;font-size:19px;color:var(--red-bright);font-weight:500}

/* gallery */
.gallery-eyebrow{left:88px;top:2267px}
.gallery-title{left:88px;top:2286px;font-size:50px}
.gallery-feature{left:88px;top:2391px;width:485px;height:428px;background:linear-gradient(180deg,#173c3a 0%,#4a2f28 40%,#6a4535 70%,#2a1f1c 100%)}
.feature-bar{left:114px;top:2682px;width:5px;height:111px;background:var(--red-bright)}
.feature-title{left:126px;top:2690px;font-size:48px;color:var(--white)}
.feature-copy{left:126px;top:2742px;font-size:16px;line-height:19px;color:var(--white);width:270px}
.gallery-tile{width:255px;height:208px}

/* testimonials */
.section-title-center{left:0;width:1200px;text-align:center;font-size:50px}
.review-card{position:absolute;top:3034px;width:326px;height:251px;background:var(--white);box-shadow:0 6px 22px rgba(0,0,0,.10);overflow:hidden}
.review-card p{position:absolute;left:27px;top:28px;width:270px;font-size:13.5px;line-height:21px;color:var(--text)}
.reviewer{position:absolute;left:27px;top:152px;display:flex;gap:12px;align-items:center}
.avatar{width:44px;height:44px;border-radius:50%;background:linear-gradient(180deg,#d6d2cf,#8a8582)}
.reviewer .name{font-size:13px;color:var(--ink);font-weight:500}
.reviewer .stars{color:#f2b01e;font-size:11px;letter-spacing:1px}
.quote-mark{position:absolute;right:-6px;bottom:-58px;font-family:'Bebas Neue',sans-serif;font-size:210px;line-height:1;color:var(--red-bright)}
.dots{left:568px;top:3328px;display:flex;gap:14px}
.dots span{width:11px;height:11px;border-radius:50%;background:#bdbdbd}
.dots span.on{background:var(--red-bright)}

/* map + footer */
.footer-band{left:0;top:4019px;width:1200px;height:509px;background:var(--red-bright)}
.map-area{left:88px;top:3567px;width:1020px;height:485px;background:linear-gradient(135deg,#ece8df 0%,#e3e6e8 50%,#efe6cf 100%)}
.newsletter-title{left:88px;top:4120px;font-size:28px;line-height:29px;color:var(--white);width:300px}
.email-field{left:783px;top:4133px;width:228px;height:33px;border:1px solid var(--white);color:var(--white);font-size:11px;padding-left:14px;display:flex;align-items:center}
.subscribe-btn{left:1020px;top:4133px;width:88px;height:33px;background:var(--white);color:var(--ink);font-size:11px;display:flex;align-items:center;justify-content:center}
.footer-rule{left:88px;width:1020px;height:1px;background:rgba(255,255,255,.7)}
.footer-brand{left:88px;top:4303px;font-size:38px;color:var(--white)}
.footer-brand .brand-mark{background:var(--white)}
.footer-tag{left:88px;top:4378px;width:250px;font-size:12px;line-height:16px;color:var(--white)}
.footer-col h4{font-family:'Bebas Neue',sans-serif;font-weight:400;font-size:30px;color:var(--white)}
.footer-col ul{list-style:none;margin-top:18px}
.footer-col li{font-size:12.5px;line-height:24px;color:var(--white)}
.contact-list li{display:flex;gap:12px;align-items:flex-start;margin-bottom:14px;line-height:16px}
.footer-legal{top:4492px;font-size:12px;color:var(--white)}
</style>
</head>
<body>

<header class="site-header">
  <div class="brand header-brand"><span class="brand-mark"></span>Ardent Summit</div>
  <nav class="main-nav">
    <a class="active" style="left:0">Home</a>
    <a style="left:83px">Services</a>
    <a style="left:182px">Abouts</a>
    <a style="left:272px">Gallery</a>
  </nav>
  <div class="btn-red" style="left:959px;top:21px;width:149px;height:45px">Get Started</div>
</header>

<section class="hero">
  <h1 class="abs display hero-title">Committed to best rooding &amp; consulting</h1>
  <p class="abs hero-copy">Lorem Ipsum is simply dummy text of the printing and typesetting industry.</p>
  <div class="btn-red" style="left:88px;top:464px;width:198px;height:42px">Book a Schedule</div>
  <div class="photo hero-photo" role="img" aria-label="Close view of terracotta and slate house roofs with dormer windows"></div>
  <div class="abs hero-rule"></div>
</section>

<section class="about">
  <div class="photo about-photo-a" role="img" aria-label="Dark timber-clad gable roof against a blue sky"></div>
  <div class="photo about-photo-b" role="img" aria-label="Roofer laying wooden sheathing boards on a roof"></div>
  <div class="abs years-badge"><span class="num">25</span><span class="label">Years of<br>practicing</span></div>
  <p class="abs eyebrow about-eyebrow">Who we are</p>
  <h2 class="abs display about-title">We're committed to roofing exellence</h2>
  <p class="abs about-copy">It is a long established fact that a reader will be distracted by the readable content of a page when looking at its layout. The point of using Lorem Ipsum is that it has a more-or-less normal distribution of letters, as opposed to using 'Content here, content here', making it look like readable English. Many desktop publishing packages and web page editors now use Lorem Ipsum as their default model text.</p>
  <div class="btn-red" style="left:554px;top:1018px;width:196px;height:40px">Book a Schedule</div>
</section>

<section class="services">
  <div class="abs services-band"></div>
  <p class="abs services-eyebrow">What we do...</p>
  <h2 class="abs display services-title">Our services<br>area</h2>
  <div class="tab current" style="top:1434px">Residential</div>
  <div class="tab" style="top:1503px">Inspections</div>
  <div class="tab" style="top:1572px">Commerical</div>

  <article class="service-card" style="left:360px">
    <span class="no">01</span>
    <svg class="icon" width="44" height="40" viewBox="0 0 44 40" fill="none" stroke="#111" stroke-width="2"><path d="M4 24 L14 6 H30 L40 24 Z"/><path d="M2 24 H42 M9 15 H35 M14 6 L11 24 M22 6 V24 M30 6 L33 24"/></svg>
    <h3>Roofing</h3>
    <p>Lorem Ipsum has been the industry's standard dummy text ever since the 1500s, when an unknown printer took a galley of type and scrambled..</p>
    <svg class="go" width="30" height="16" viewBox="0 0 30 16" fill="none" stroke="#111" stroke-width="2"><path d="M1 8 H28 M21 1 L28 8 L21 15"/></svg>
  </article>
  <article class="service-card raised" style="left:623px">
    <span class="no">02</span>
    <svg class="icon" width="44" height="44" viewBox="0 0 44 44" fill="none" stroke="#111" stroke-width="2"><path d="M6 38 L30 14 M26 8 a8 8 0 1 0 10 10 l-5-1 -3-3 -1-5z"/><path d="M8 6 L22 20 M6 10 L10 6 M24 24 L38 38 L34 42 L20 28"/></svg>
    <h3>Roof Repairs</h3>
    <p>Lorem Ipsum has been the industry's standard dummy text ever since the 1500s, when an unknown printer took a galley of type and scrambled..</p>
    <svg class="go" width="30" height="16" viewBox="0 0 30 16" fill="none" stroke="#111" stroke-width="2"><path d="M1 8 H28 M21 1 L28 8 L21 15"/></svg>
  </article>
  <article class="service-card" style="left:885px">
    <span class="no">03</span>
    <svg class="icon" width="44" height="44" viewBox="0 0 44 44" fill="none" stroke="#111" stroke-width="2"><path d="M6 10 H28 V20 H20 V34 a6 6 0 0 0 6 6 H36 V30"/><path d="M6 10 V4 H28 V10"/><path d="M34 22 q-4 6 0 8 q4-2 0-8z"/></svg>
    <h3>Gutters</h3>
    <p>Lorem Ipsum has been the industry's standard dummy text ever since the 1500s, when an unknown printer took a galley of type and scrambled..</p>
    <svg class="go" width="30" height="16" viewBox="0 0 30 16" fill="none" stroke="#111" stroke-width="2"><path d="M1 8 H28 M21 1 L28 8 L21 15"/></svg>
  </article>
</section>

<section class="products">
  <p class="abs eyebrow products-eyebrow">Explore</p>
  <h2 class="abs display products-title">Our products</h2>
  <div class="arrow-btn outline"><svg width="22" height="12" viewBox="0 0 22 12" fill="none" stroke="#111" stroke-width="2"><path d="M21 6 H2 M7 1 L2 6 L7 11"/></svg></div>
  <div class="arrow-btn filled"><svg width="22" height="12" viewBox="0 0 22 12" fill="none" stroke="#fff" stroke-width="2"><path d="M1 6 H20 M15 1 L20 6 L15 11"/></svg></div>
  <div class="photo product-photo" style="left:88px;background:linear-gradient(160deg,#c8ccd1,#6e7379 60%,#3b3f44)" role="img" aria-label="Roofers in hard hats working on a metal roof"></div>
  <div class="photo product-photo" style="left:440px;background:linear-gradient(180deg,#9aa3ad,#5b5f64 50%,#b88a5c)" role="img" aria-label="New timber-framed gable with dark metal roofing"></div>
  <div class="photo product-photo" style="left:788px;background:linear-gradient(160deg,#c9cdd2,#7c8188 50%,#c9d33a)" role="img" aria-label="Roofer in yellow hard hat installing roof panels"></div>
  <span class="product-name" style="left:88px">Spryers</span>
  <span class="product-name" style="left:440px">Core Cutting Tools</span>
  <span class="product-name" style="left:788px">Leaf Blower</span>
</section>

<section class="gallery">
  <p class="abs eyebrow gallery-eyebrow">Our Gallery</p>
  <h2 class="abs display gallery-title">Recent projects</h2>
  <div class="photo gallery-feature" role="img" aria-label="Stacks of clay roof tiles"></div>
  <div class="abs feature-bar"></div>
  <h3 class="abs display feature-title">Roofing services</h3>
  <p class="abs feature-copy">Lorem Ipsum is simply dummy text of the printing</p>
  <div class="photo gallery-tile" style="left:585px;top:2391px;background:linear-gradient(160deg,#8fb6db,#c7e04a 50%,#4a4c50)" role="img" aria-label="Roofer in hi-vis sealing a roof edge"></div>
  <div class="photo gallery-tile" style="left:853px;top:2391px;background:linear-gradient(160deg,#b7bcc2,#c59a5c 55%,#8a6a46)" role="img" aria-label="Two workers laying membrane on a roof"></div>
  <div class="photo gallery-tile" style="left:585px;top:2611px;background:linear-gradient(180deg,#4e6f93,#8aa1b8 45%,#8a4a2e)" role="img" aria-label="Tiled roof with chimney at dusk"></div>
  <div class="photo gallery-tile" style="left:853px;top:2611px;background:linear-gradient(160deg,#a85a48,#7b3b31 50%,#b76b58)" role="img" aria-label="Close-up of red clay roof tiles"></div>
</section>

<section class="testimonials">
  <h2 class="abs display section-title-center" style="top:2942px">Testimonials</h2>
  <article class="review-card" style="left:88px">
    <p>Lorem Ipsum is simply dummy text of the printing and Lorem Ipsum has been the industry's standard dummy text ever since the 1500s</p>
    <div class="reviewer"><div class="avatar" role="img" aria-label="Reviewer portrait"></div><div><div class="name">Mara Lindqvist</div><div class="stars">★★★★★</div></div></div>
    <span class="quote-mark">“</span>
  </article>
  <article class="review-card" style="left:435px">
    <p>Lorem Ipsum is simply dummy text of the printing and Lorem Ipsum has been the industry's standard dummy text ever since the 1500s</p>
    <div class="reviewer"><div class="avatar" role="img" aria-label="Reviewer portrait"></div><div><div class="name">Mara Lindqvist</div><div class="stars">★★★★★</div></div></div>
    <span class="quote-mark">“</span>
  </article>
  <article class="review-card" style="left:783px">
    <p>Lorem Ipsum is simply dummy text of the printing and Lorem Ipsum has been the industry's standard dummy text ever since the 1500s</p>
    <div class="reviewer"><div class="avatar" role="img" aria-label="Reviewer portrait"></div><div><div class="name">Mara Lindqvist</div><div class="stars">★★★★★</div></div></div>
    <span class="quote-mark">“</span>
  </article>
  <div class="abs dots"><span></span><span class="on"></span><span></span></div>
</section>

<section class="service-map">
  <h2 class="abs display section-title-center" style="top:3468px">Service area map</h2>
  <div class="abs footer-band"></div>
  <div class="photo map-area" role="img" aria-label="Street map of the service area with the office location pinned"></div>
</section>

<footer class="site-footer">
  <h3 class="abs display newsletter-title">Join our newsletter to keep up to date with us!</h3>
  <div class="abs email-field">Enter you email</div>
  <div class="abs subscribe-btn">Subscribe</div>
  <div class="abs footer-rule" style="top:4220px"></div>

  <div class="brand footer-brand"><span class="brand-mark"></span>Ardent Summit</div>
  <p class="abs footer-tag">Lorem Ipsum is simply dummy text of the printing</p>

  <div class="abs footer-col" style="left:772px;top:4250px">
    <h4>Company</h4>
    <ul><li>Home</li><li>About us</li><li>Services</li><li>Products</li><li>Gallery</li><li>Map</li></ul>
  </div>
  <div class="abs footer-col" style="left:940px;top:4250px">
    <h4>Contact us</h4>
    <ul class="contact-list">
      <li><svg width="12" height="16" viewBox="0 0 12 16" fill="#fff"><path d="M6 0a6 6 0 0 0-6 6c0 4.5 6 10 6 10s6-5.5 6-10a6 6 0 0 0-6-6zm0 8.5A2.5 2.5 0 1 1 6 3.5a2.5 2.5 0 0 1 0 5z"/></svg><span>1234, xyz Lorem<br>Ipsum is simply</span></li>
      <li><svg width="13" height="13" viewBox="0 0 24 24" fill="#fff"><path d="M6.6 10.8a15 15 0 0 0 6.6 6.6l2.2-2.2a1 1 0 0 1 1-.25 11.4 11.4 0 0 0 3.6.57 1 1 0 0 1 1 1V20a1 1 0 0 1-1 1A17 17 0 0 1 3 4a1 1 0 0 1 1-1h3.5a1 1 0 0 1 1 1c0 1.25.2 2.45.57 3.57a1 1 0 0 1-.25 1z"/></svg><span>(012)-555-01920</span></li>
      <li><svg width="14" height="11" viewBox="0 0 14 11" fill="#fff"><path d="M0 0h14v11H0z"/><path d="M0 0l7 6 7-6" stroke="#E8242B" fill="none"/></svg><span>hello@ardentsummit.co</span></li>
    </ul>
  </div>

  <div class="abs footer-rule" style="top:4469px"></div>
  <p class="abs footer-legal" style="left:88px">Copyright 2023 | All Rights Reserved.</p>
  <p class="abs footer-legal" style="left:838px">Privacy Policy</p>
  <p class="abs footer-legal" style="left:971px">Terms of Condition</p>
</footer>

</body>
</html>
```